DeskPilot.dk Frontpage design

I'm in the process of starting a It-course website, based in Denmark. The web site Url is - www.deskpilot.dk

The services are:
- Online courses (This is the main service and the most important)
- One to One courses
- Webinar

I need a frontpage design a simple design, but it must shows professionalism. I have no preference in color, but I like white space.

In Denmark the established competitors are:
- www.trivano.dk (Biggest competitor)
- www.brandlime.dk/online-kurser
- www.selvanu.dk

Target Market(s)

Mainly companies (B to B), but there are also a small number of private customers

Industry/Entity Type

Online it courses and one to one consulting

Number of Pages Required

1 page

Font styles to use
Sans Serif

Requirements
Must have
• A professional design, white space

```html
<!DOCTYPE html>
<html lang="da">
<head>
<meta charset="utf-8">
<title>DeskPilot.dk – Online it-kurser</title>
<link href="https://fonts.googleapis.com/css2?family=Inter:wght@400;500;600;700;800&display=swap" rel="stylesheet">
<style>
:root{
  --green:#2ecc6a;
  --green-dark:#1fa955;
  --ink:#0f1a15;
  --night:#0c1712;
  --text:#1e2622;
  --muted:#5f6b66;
  --line:#e3e8e5;
  --mint:#ebf7f0;
  --white:#ffffff;
}
*{box-sizing:border-box;margin:0;padding:0}
html,body{width:1200px;height:3484px;overflow:hidden}
body{font-family:"Inter",Arial,sans-serif;color:var(--text);background:var(--white);position:relative}
a{color:inherit;text-decoration:none}
.abs{position:absolute}

/* top bar */
.topbar{left:0;top:0;width:1200px;height:30px;background:#07110c;color:#cfd8d3;font-size:12px;display:flex;align-items:center;justify-content:center}
.topbar b{color:var(--green);font-weight:600;margin-left:6px;text-decoration:underline}
.topbar .socials{position:absolute;right:40px;top:9px;display:flex;gap:12px}
.dot{width:12px;height:12px;border-radius:50%;background:#cfd8d3}

/* hero */
.hero{left:0;top:30px;width:1200px;height:578px;background:linear-gradient(110deg,#0d1a14 0%,#1a2a23 45%,#2d3a34 70%,#1a2621 100%)}
.nav{left:0;top:30px;width:1200px;height:104px;display:flex;align-items:center;padding:0 56px}
.logo{font-size:30px;font-weight:800;color:var(--green);letter-spacing:-0.5px}
.menu{display:flex;gap:26px;margin-left:70px;color:#fff;font-size:15px;font-weight:500}
.signin{margin-left:auto;background:#111c17;color:#fff;border:1px solid #3a4a43;border-radius:22px;padding:11px 24px;font-size:14px;font-weight:600}
.hero-copy{left:176px;top:196px;width:440px;color:#fff}
.hero-copy h1{font-size:42px;line-height:1.15;font-weight:800;letter-spacing:-0.5px}
.hero-copy p{margin-top:20px;font-size:15px;line-height:1.55;color:#d8e0dc;width:420px}
.hero-actions{margin-top:28px;display:flex;gap:18px}
.btn{display:inline-flex;align-items:center;justify-content:center;height:48px;padding:0 28px;border-radius:26px;font-size:15px;font-weight:600}
.btn-green{background:var(--green);color:#fff}
.btn-outline{border:1.5px solid #fff;color:#fff}
.btn-dark{background:var(--ink);color:#fff}
.hero-video{left:660px;top:216px;width:420px;height:272px;border:3px solid var(--green);border-radius:18px;background:linear-gradient(135deg,#26352e,#121d18 60%,#2b3a33);overflow:hidden}
.play{position:absolute;left:50%;top:50%;width:66px;height:66px;margin:-33px 0 0 -33px;border-radius:50%;background:rgba(0,0,0,.55);display:flex;align-items:center;justify-content:center}

/* section headings */
.eyebrow{font-size:13px;letter-spacing:2px;color:var(--muted);text-transform:uppercase;font-weight:500}
.center{text-align:center;left:0;width:1200px}
.h2{font-size:30px;font-weight:800;color:var(--ink);letter-spacing:-0.4px;line-height:1.2}

/* course cards */
.card{top:780px;width:330px;height:380px;border:1px solid var(--line);border-radius:20px;background:#fff;box-shadow:0 6px 24px rgba(15,26,21,.06);padding:16px}
.card .thumb{height:188px;border-radius:12px}
.card h3{margin-top:22px;font-size:18px;font-weight:700;color:var(--ink)}
.card p{margin-top:10px;font-size:14px;line-height:1.55;color:var(--muted)}

/* webinar */
.webinar-video{left:164px;top:1356px;width:372px;height:232px;border-radius:12px;background:linear-gradient(120deg,#0e1512,#2c3833 55%,#101814)}
.webinar-text{left:580px;top:1352px;width:480px}
.webinar-text p{font-size:13.5px;line-height:1.6;color:var(--muted)}
.webinar-text .btn{margin-top:20px}

/* why */
.why{left:0;top:1672px;width:1200px;height:400px;background:var(--mint)}
.why-intro{left:56px;top:1760px;width:380px}
.why-intro h2{margin-top:12px;font-size:30px;line-height:1.2}
.why-intro p{margin-top:20px;font-size:14px;line-height:1.6;color:var(--muted)}
.feature{width:300px;display:flex;gap:18px}
.feature .ico{flex:none;width:60px;height:60px;border-radius:50%;background:#fff;border:1px solid #d2e8db;display:flex;align-items:center;justify-content:center}
.feature h4{font-size:16px;font-weight:700;color:var(--ink);margin-top:4px}
.feature p{font-size:13.5px;line-height:1.5;color:var(--muted);margin-top:6px}

/* one to one */
.oto-photo{left:56px;top:2280px;width:504px;height:280px;border-radius:14px;background:linear-gradient(135deg,#8a8f86,#4f5b55 50%,#b8b2a4)}
.oto-copy{left:608px;top:2136px;width:520px}
.oto-copy h2{margin-top:14px;font-size:32px;line-height:1.22}
.oto-copy p{margin-top:22px;font-size:14px;line-height:1.6;color:var(--muted);width:440px}
.oto-copy .btn{margin-top:26px}

/* blog */
.viewall{left:1080px;top:2688px;font-size:14px;font-weight:500;text-decoration:underline;color:var(--ink)}
.post{top:2720px;width:336px;height:400px;border:1px solid var(--line);border-radius:20px;background:#fff;box-shadow:0 6px 24px rgba(15,26,21,.06);padding:14px}
.post .thumb{height:176px;border-radius:10px}
.post .date{margin-top:28px;font-size:15px;font-weight:700;color:var(--green);letter-spacing:.5px}
.post h3{margin-top:8px;font-size:19px;font-weight:700;color:var(--ink)}
.post p{margin-top:8px;font-size:14px;line-height:1.55;color:var(--muted)}

/* footer */
.footer{left:0;top:3148px;width:1200px;height:336px;background:var(--night);color:#c8d2cd}
.f-col{top:3212px;font-size:14px;line-height:1.6}
.f-col h5{font-size:16px;font-weight:700;color:var(--green);margin-bottom:12px}
.f-col ul{list-style:none}
.f-col li{margin-bottom:6px;color:#fff}
.f-socials{display:flex;gap:14px;margin-top:18px}
.f-socials .dot{width:20px;height:20px;background:#c8d2cd}
.input{margin-top:18px;width:270px;height:44px;border-radius:22px;background:#1b2822;border:1px solid #2c3a34;color:#7d8a84;font-size:13px;display:flex;align-items:center;padding:0 20px}
.submit{margin-top:12px;width:270px;height:44px;border-radius:22px;background:var(--green);color:#fff;font-weight:600;font-size:15px;display:flex;align-items:center;justify-content:center;gap:10px}
.f-rule{left:56px;top:3420px;width:1088px;height:1px;background:#24322b}
.copy{left:0;top:3440px;width:1200px;text-align:center;font-size:13px;color:#7d8a84}
</style>
</head>
<body>

<div class="abs topbar">Styrk dine it kundskaber med “just-in-time” learning. <b>Read More</b>
  <div class="socials"><span class="dot"></span><span class="dot"></span><span class="dot"></span><span class="dot"></span></div>
</div>

<section class="abs hero" role="img" aria-label="Mørkt baggrundsfoto af en person der arbejder ved en bærbar computer"></section>
<nav class="abs nav">
  <a class="logo" href="#">deskpilot</a>
  <div class="menu"><a>Courses</a><a>Webinar</a><a>One to One</a><a>Questions</a><a>Blog</a><a>About</a><a>Contact</a></div>
  <a class="signin">Sign In</a>
</nav>
<div class="abs hero-copy">
  <h1>Styrk dine it kundskaber med “just-in-time” learning</h1>
  <p>Jeg tilbyder online kurser og webinarer med et klart fokus, eller hvad med online “En til En” undervisning</p>
  <div class="hero-actions"><a class="btn btn-green">Get Started</a><a class="btn btn-outline">Our Services</a></div>
</div>
<div class="abs hero-video" role="img" aria-label="Videoklip af en underviser ved computeren">
  <div class="play"><svg width="24" height="26" viewBox="0 0 24 26"><path d="M4 2l18 11L4 24z" fill="#fff"/></svg></div>
</div>

<div class="abs center eyebrow" style="top:668px">Udvalgte kurser</div>
<h2 class="abs center h2" style="top:700px">Find dit næste online kursus her</h2>

<article class="abs card" style="left:56px">
  <div class="thumb" role="img" aria-label="Illustration af et gult søjlediagram" style="background:linear-gradient(135deg,#fff6d6,#f6d36a)"></div>
  <h3>Vizora BI på én time</h3>
  <p>Er det muligt at lære Vizora BI på kun én time? Nok ikke, men jeg kan give dig en introduktion.</p>
</article>
<article class="abs card" style="left:435px">
  <div class="thumb" role="img" aria-label="Illustration af regneark og kode på grøn baggrund" style="background:linear-gradient(135deg,#1f7a46,#2f9a5a)"></div>
  <h3>Kodeflow for Regnia brugere</h3>
  <p>Hvordan kommer du som Regnia bruger i gang med at bruge Kodeflow.</p>
</article>
<article class="abs card" style="left:814px">
  <div class="thumb" role="img" aria-label="Illustration af et programmeringssprog på lyseblå baggrund" style="background:linear-gradient(135deg,#e6f1fb,#b9cfe6)"></div>
  <h3>Statlang introduktion</h3>
  <p>Introduktion til Statlang programmering. Lorem ipsum dolor sit amet, consectetur.</p>
</article>

<div class="abs center eyebrow" style="top:1214px">Our webinar classes</div>
<h2 class="abs center h2" style="top:1244px">Find det, der fascinerer dig, når du<br>udforsker disse webinarklasser.</h2>
<div class="abs webinar-video" role="img" aria-label="Videoklip fra et webinar med en person ved et skrivebord">
  <div class="play" style="width:56px;height:56px;margin:-28px 0 0 -28px"><svg width="20" height="22" viewBox="0 0 24 26"><path d="M4 2l18 11L4 24z" fill="#fff"/></svg></div>
</div>
<div class="abs webinar-text">
  <p>Det er ikke kun på prisen at webinarer slår traditionelle kurser! Du får den samme høje kvalitet på et webinar som på et traditionelt kursus, endda med den fordel at du kan se dem og igen. Det bedste af det hele er du ikke behøver at flytte dig fra dit faste sted. Nemo enim ipsam voluptatem quia voluptas sit aspernatur aut odit aut fugit, sed quia consequuntur magni dolores eos qui ratione voluptatem sequi nesciunt.</p>
  <a class="btn btn-green">Webinar Course</a>
</div>

<section class="abs why"></section>
<div class="abs why-intro">
  <div class="eyebrow">Hvorfor vælge os</div>
  <h2 class="h2">Mange IT-kurser, men hvorfor vælge DeskPilot?</h2>
  <p>I have been teaching a lot of happy students since 1995. Lorem ipsum dolor sit amet, consectetur adipiscing elit. Adipiscing faucibus consectetur nam vitae sem. Et nullam quis varius velit, egestas.</p>
</div>
<div class="abs feature" style="left:480px;top:1748px">
  <div class="ico"><svg width="26" height="26" viewBox="0 0 24 24" fill="none" stroke="#1fa955" stroke-width="1.8"><rect x="3" y="6" width="18" height="13" rx="2"/><path d="M16 12h5"/></svg></div>
  <div><h4>God økonomi</h4><p>Prisen på et online kursus er lavere end et fysisk kursus</p></div>
</div>
<div class="abs feature" style="left:828px;top:1748px">
  <div class="ico"><svg width="26" height="26" viewBox="0 0 24 24" fill="none" stroke="#1fa955" stroke-width="1.8"><path d="M5 12l5 5 9-10"/></svg></div>
  <div><h4>Lær nye færdigheder</h4><p>Styrk dine kompetencer på et online kursus nu</p></div>
</div>
<div class="abs feature" style="left:480px;top:1890px">
  <div class="ico"><svg width="26" height="26" viewBox="0 0 24 24" fill="none" stroke="#1fa955" stroke-width="1.8"><circle cx="12" cy="12" r="8"/><path d="M12 8v4l3 2"/></svg></div>
  <div><h4>God økonomi</h4><p>Du slipper for spildtid og besparelser kan bruges du skal have til frokost</p></div>
</div>
<div class="abs feature" style="left:828px;top:1890px">
  <div class="ico"><svg width="26" height="26" viewBox="0 0 24 24" fill="none" stroke="#1fa955" stroke-width="1.8"><rect x="3" y="4" width="18" height="13" rx="2"/><path d="M8 21h8M12 17v4"/></svg></div>
  <div><h4>Designed in a browser</h4><p>Designing in a browser allows rapid development and saves cost</p></div>
</div>

<div class="abs oto-photo" role="img" aria-label="Foto af deltagere der sidder ved et bord på et kursus"></div>
<div class="abs oto-copy">
  <div class="eyebrow">One to one course</div>
  <h2 class="h2">Targeted teaching at just the right time will make you better and faster for your assignments</h2>
  <p>Lorem ipsum dolor sit amet consectetur adipiscing elit. Enim mauris elementum mi proin rhoncus vitae tempor mi. Lectus bibendum purus at ut dignissim enim placerat justo ipsum. Pellentesque eget et, non et rutrum.</p>
  <a class="btn btn-dark">One to One</a>
</div>

<div class="abs center eyebrow" style="top:2600px">Our blogs</div>
<h2 class="abs center h2" style="top:2628px">Check out our news and interests</h2>
<a class="abs viewall">View All</a>

<article class="abs post" style="left:56px">
  <div class="thumb" role="img" aria-label="Skærmbillede af en rapport med tabel" style="background:linear-gradient(180deg,#dfe8f5,#9cb6dc)"></div>
  <div class="date">JULY 04, 2022</div>
  <h3>Current sum</h3>
  <p>Er det muligt at lære Vizora BI på kun én time? Nok ikke, men jeg kan give dig en introduktion.</p>
</article>
<article class="abs post" style="left:432px">
  <div class="thumb" role="img" aria-label="Illustration af en arbejdsplads med skærm" style="background:linear-gradient(180deg,#d8f0f4,#6fb7c6)"></div>
  <div class="date">JULY 04, 2022</div>
  <h3>Lorem ipsum dolor sit amet</h3>
  <p>Lorem ipsum dolor sit amet, consectetur adipiscing elit nam vitae sem.</p>
</article>
<article class="abs post" style="left:808px">
  <div class="thumb" role="img" aria-label="Foto af hænder der skriver på en bærbar computer" style="background:linear-gradient(135deg,#c9b9a6,#6e5e52)"></div>
  <div class="date">JULY 04, 2022</div>
  <h3>Lorem ipsum dolor sit amet</h3>
  <p>Lorem ipsum dolor sit amet, consectetur adipiscing elit nam vitae sem.</p>
</article>

<footer class="abs footer"></footer>
<div class="abs f-col" style="left:56px;width:320px">
  <div class="logo" style="font-size:30px">deskpilot</div>
  <div class="f-socials"><span class="dot"></span><span class="dot"></span><span class="dot"></span><span class="dot"></span></div>
  <p style="margin-top:18px;color:#c8d2cd">Lorem ipsum dolor sit amet, consectetur adipiscing elit, sed do eiusmod tempor incididunt ut labore et dolore magna aliqua. Ut enim ad minim veniam</p>
</div>
<div class="abs f-col" style="left:440px"><h5>DeskPilot</h5><ul><li>Courses</li><li>Webinar</li><li>One to one</li><li>Questions</li></ul></div>
<div class="abs f-col" style="left:608px"><h5>About</h5><ul><li>Support</li><li>Contact</li><li>Terms</li><li>Blog</li></ul></div>
<div class="abs f-col" style="left:860px;width:290px">
  <h5>Subscribe to our Newsletter</h5>
  <p style="color:#fff">Lorem ipsum dolor sit amet, consectetur adipiscing elit, sed do eiusmod.</p>
  <div class="input">Enter email address</div>
  <div class="submit">Submit <svg width="16" height="12" viewBox="0 0 16 12" fill="none" stroke="#fff" stroke-width="2"><path d="M1 6h13M9 1l5 5-5 5"/></svg></div>
</div>
<div class="abs f-rule"></div>
<div class="abs copy">Copyright © 2022</div>

</body>
</html>
```